Creative & Professional Business Card for hair salon

We are looking to update our business cards. Our salon is creative, modern, progressive and professional and looking for a design that will reflect this.

```html
<!DOCTYPE html>
<html lang="en">
<head>
<meta charset="utf-8">
<title>Lofty Locks – Business Card</title>
<link rel="stylesheet" href="https://fonts.googleapis.com/css2?family=Montserrat:wght@300;400&display=swap">
<style>
  :root {
    --page: #eef1f3;
    --sky: #6a9fb6;
    --sky-deep: #5b8ea7;
    --sky-light: #8fbccd;
    --cloud-soft: #dfecf2;
    --ink: #5e93aa;
    --field: rgba(255, 255, 255, 0.38);
    --field-line: rgba(255, 255, 255, 0.9);
    --frame: #8a8f93;
  }
  * { box-sizing: border-box; margin: 0; padding: 0; }
  html, body { width: 1200px; height: 622px; overflow: hidden; }
  body {
    background: var(--page);
    font-family: "Montserrat", sans-serif;
    position: relative;
  }

  /* ---------- front ---------- */
  .card-front {
    position: absolute;
    left: 70px; top: 126px;
    width: 620px; height: 370px;
    border: 2px solid var(--frame);
    overflow: hidden;
  }
  .sky-photo {
    position: absolute; inset: 0;
    background: radial-gradient(ellipse 42% 32% at 50% 48%, #f4f8fa 0%, var(--cloud-soft) 45%, rgba(143, 188, 205, 0) 100%),
                linear-gradient(180deg, var(--sky-light) 0%, var(--sky) 50%, var(--sky-deep) 100%);
  }
  .brand {
    position: absolute;
    left: 0; right: 0; top: 162px;
    text-align: center;
    color: var(--ink);
    font-weight: 400;
    font-size: 28px;
    letter-spacing: 0.3px;
  }

  /* ---------- back ---------- */
  .card-back {
    position: absolute;
    left: 800px; top: 36px;
    width: 330px; height: 552px;
    background: #ffffff;
    border: 2px solid var(--frame);
    overflow: hidden;
  }
  .back-sky {
    position: absolute; left: 0; top: 0; width: 100%; height: 250px;
    background: var(--sky);
  }
  .cloud-photo {
    position: absolute; left: 0; top: 250px; width: 100%; height: 110px;
    background: linear-gradient(180deg, var(--sky) 0%, var(--cloud-soft) 55%, #ffffff 100%);
  }
  .appointment-title {
    position: absolute;
    left: 36px; top: 30px;
    color: #ffffff;
    font-weight: 300;
    font-size: 19px;
  }
  .slot {
    position: absolute;
    left: 36px;
    width: 258px; height: 40px;
    background: var(--field);
    border-radius: 6px;
    color: #ffffff;
    font-weight: 300;
    font-size: 16px;
  }
  .slot span { position: absolute; }
  .slot .date { left: 10px; top: 10px; }
  .slot .time { left: 148px; top: 6px; padding-left: 6px; line-height: 28px; border-left: 1.5px solid var(--field-line); }
  .slot-1 { top: 70px; }
  .slot-2 { top: 129px; }
  .slot-3 { top: 189px; }

  .contact-list {
    position: absolute;
    left: 34px; top: 322px;
    list-style: none;
  }
  .contact-list li {
    display: flex; align-items: center;
    height: 42px;
    color: var(--ink);
    font-weight: 300;
    font-size: 14px;
  }
  .contact-list svg { width: 18px; height: 18px; margin-right: 10px; flex: none; }
</style>
</head>
<body>

<section class="card-front" aria-label="Card front">
  <div class="sky-photo" role="img" aria-label="Photograph of soft white clouds in a blue sky"></div>
  <p class="brand">Lofty Locks by Mia Corran</p>
</section>

<section class="card-back" aria-label="Card back">
  <div class="back-sky"></div>
  <div class="cloud-photo" role="img" aria-label="Photograph of a band of white clouds"></div>

  <p class="appointment-title">Your next appointment is</p>
  <div class="slot slot-1"><span class="date">d/</span><span class="time">t/</span></div>
  <div class="slot slot-2"><span class="date">d/</span><span class="time">t/</span></div>
  <div class="slot slot-3"><span class="date">d/</span><span class="time">t/</span></div>

  <ul class="contact-list">
    <li>
      <svg viewBox="0 0 18 18" fill="none" stroke="currentColor" stroke-width="1.3"><path d="M2 9 9 3l7 6"/><path d="M4 8v8h10V8"/><rect x="7.5" y="11" width="3" height="5"/></svg>
      5/12 Harbour Lane, Kelvale
    </li>
    <li>
      <svg viewBox="0 0 18 18" fill="none" stroke="currentColor" stroke-width="1.3"><path d="M4 2h3l1.5 4-2 1.2a9 9 0 0 0 4.3 4.3l1.2-2 4 1.5v3a1.5 1.5 0 0 1-1.5 1.5A13 13 0 0 1 2.5 3.5 1.5 1.5 0 0 1 4 2z"/></svg>
      07 5550 1234
    </li>
    <li>
      <svg viewBox="0 0 18 18" fill="none" stroke="currentColor" stroke-width="1.3"><rect x="2" y="4" width="14" height="10"/><path d="M2 4l7 6 7-6"/></svg>
      salon@loftylocks.com.au
    </li>
    <li>
      <svg viewBox="0 0 18 18" fill="none" stroke="currentColor" stroke-width="1.3"><circle cx="9" cy="9" r="7"/><ellipse cx="9" cy="9" rx="3" ry="7"/><path d="M2 9h14"/></svg>
      www.loftylocks.com.au
    </li>
    <li>
      <svg viewBox="0 0 18 18" fill="none" stroke="currentColor" stroke-width="1.3"><rect x="2.5" y="2.5" width="13" height="13" rx="1.5"/></svg>
      LoftyLocksbyMiaCorran
    </li>
  </ul>
</section>

</body>
</html>
```